Website Design for Employee Moral and Happiness Company

Looking for a clean website design that explains our features in a step by step manner so our visitors know exactly what our site does before logging in.

The site is called "Velasto". See logo design and video for a sample of style and an overview of what we do.

Target Market(s)

Business owners that are looking to retain employees.

Number of Pages Required

1 page

```html
<!DOCTYPE html>
<html lang="en">
<head>
<meta charset="utf-8">
<title>Velasto — Improve Your Employee Morale</title>
<link rel="stylesheet" href="https://fonts.googleapis.com/css2?family=Arvo:wght@400;700&family=Montserrat:ital,wght@0,400;0,500;0,600;0,700;1,400&display=swap">
<style>
:root{
  --orange:#ff6a00;
  --navy:#1f3556;
  --ink:#111111;
  --text:#444444;
  --bg:#fdfbf8;
  --beige:#e8dfd0;
  --card:#f5f1eb;
  --white:#ffffff;
}
*{margin:0;padding:0;box-sizing:border-box}
html,body{width:1200px;height:4313px;overflow:hidden}
body{background:var(--bg);font-family:"Montserrat",sans-serif;color:var(--text);position:relative}
.abs{position:absolute}
.btn{position:absolute;display:inline-flex;align-items:center;justify-content:center;gap:8px;background:var(--orange);color:#fff;font-size:12px;font-weight:600;border-radius:22px;height:38px;padding:0 24px;text-transform:uppercase;letter-spacing:.2px;white-space:nowrap}
.arrow{width:12px;height:10px}

/* nav */
.logo{left:60px;top:12px;font-family:"Arvo",serif;font-weight:700;font-size:36px;color:var(--ink)}
.nav{left:450px;top:30px;display:flex;gap:30px;font-size:11px;font-weight:600;color:var(--ink)}
.login{left:900px;top:20px;height:36px;padding:0 18px;border-radius:18px;background:#efebe5;font-size:11px;font-weight:600;color:var(--ink);display:flex;align-items:center;gap:6px}
.demo-top{left:998px;top:20px;height:36px;font-size:11px;padding:0 20px}

/* hero */
.hero-circle{left:640px;top:-140px;width:820px;height:820px;border-radius:50%;background:#fff;box-shadow:-18px 18px 0 #f1ece5}
.hero-art{left:660px;top:80px;width:520px;height:560px;border-radius:40px 40px 8px 8px;background:linear-gradient(160deg,#ffe2cc 0%,#ffb27a 45%,#2a4068 100%)}
.hero-title{left:60px;top:212px;font-family:"Arvo",serif;font-weight:700;font-size:72px;line-height:100px;color:var(--ink);white-space:nowrap}
.hero-title .outline{color:transparent;-webkit-text-stroke:1.5px var(--ink);font-weight:400}
.hero-sub{left:60px;top:432px;font-size:16px;color:#333}
.get-started{left:60px;top:480px;height:40px}
.explainer{left:232px;top:488px;display:flex;align-items:center;gap:10px;font-size:12px;font-weight:600;color:var(--ink)}
.play{width:22px;height:22px;border-radius:50%;background:var(--orange);display:flex;align-items:center;justify-content:center}
.trusted{left:60px;top:612px;display:flex;align-items:center;gap:36px;font-size:12px;font-weight:600;color:#333}
.trusted .brand{display:flex;align-items:center;gap:6px;font-size:14px;font-weight:600;color:#555}
.trusted .sq{width:12px;height:12px;background:#9a9a9a}

/* section heads */
.eyebrow{font-size:13px;font-weight:500;color:var(--ink);text-transform:uppercase;text-align:center;width:100%;left:0}
.eyebrow span{background:var(--orange);color:#fff;padding:0 2px}
.section-title{left:0;width:100%;text-align:center;font-family:"Arvo",serif;font-weight:700;font-size:42px;line-height:56px;color:var(--ink)}

/* features */
.connector{left:0;top:930px;width:1200px;height:1100px}
.feature-art{border-radius:50%;box-shadow:0 0 0 14px #fff,0 14px 40px rgba(0,0,0,.08)}
.art1{left:160px;top:1050px;width:340px;height:340px;background:radial-gradient(circle at 55% 40%,#f4c9a8 0,#7dc4b8 45%,#1f3556 100%)}
.art2{left:690px;top:1530px;width:370px;height:300px;border-radius:48% 48% 20px 20px;background:linear-gradient(170deg,#fff 0%,#8fc9c0 45%,#2a3f63 100%)}
.art2-base{left:660px;top:1818px;width:450px;height:30px;border-radius:15px;background:var(--orange)}
.art3{left:134px;top:2010px;width:376px;height:360px;border-radius:50%;background:linear-gradient(135deg,#e8dfd0 0%,#f4a867 45%,#2a3f63 100%)}
.orange-dot{border-radius:50%;background:var(--orange)}
.f-label{font-size:12px;font-weight:600;color:var(--orange);text-transform:uppercase}
.f-title{font-family:"Arvo",serif;font-weight:700;font-size:30px;line-height:44px;color:var(--ink)}
.f-body{font-size:11.5px;line-height:24px;color:#555;width:390px}

/* about */
.about-box{left:60px;top:2497px;width:1080px;height:524px;border-radius:26px;background:var(--beige)}
.about-title{top:2586px}
.planner-art{left:200px;top:2765px;width:780px;height:455px;border-radius:16px;background:linear-gradient(180deg,#f8f4ee 0%,#e9e2d6 70%,#bdb7af 100%);box-shadow:0 8px 30px rgba(0,0,0,.08)}

/* reviews */
.review{top:3440px;width:345px;height:343px;background:var(--card);padding:36px 30px}
.stars{color:var(--orange);font-size:13px;letter-spacing:2px}
.r-title{margin-top:14px;font-family:"Arvo",serif;font-weight:700;font-size:19px;color:var(--ink)}
.r-body{margin-top:10px;font-size:11px;line-height:24px;font-style:italic;color:#555}
.r-name{margin-top:16px;font-family:"Arvo",serif;font-size:19px;color:var(--orange)}
.r-role{margin-top:4px;font-size:10px;font-weight:600;color:#555}
.quote{position:absolute;right:30px;bottom:38px;font-family:"Arvo",serif;font-size:80px;line-height:40px;color:#ddd5c9;height:40px}

/* newsletter */
.news-band{left:0;top:3830px;width:1200px;height:420px}
.news-title{top:4060px}
.subscribe{left:355px;top:4152px;width:490px;height:44px;border-radius:22px;background:#fff;box-shadow:0 4px 18px rgba(0,0,0,.08);display:flex;align-items:center;padding-left:26px;font-size:12px;color:#555}
.subscribe .btn{right:0;top:3px;height:38px;left:auto}

/* footer */
.footer-nav{left:60px;top:4270px;display:flex;gap:30px;font-size:11px;font-weight:600;color:var(--ink)}
.socials{left:544px;top:4262px;display:flex;gap:10px}
.socials span{width:32px;height:32px;border-radius:50%;background:var(--orange)}
.socials span+span{background:#ddd5c9}
.copy{right:60px;top:4270px;font-family:"Arvo",serif;font-size:11px;color:var(--ink)}
</style>
</head>
<body>

<div class="abs hero-circle"></div>
<div class="abs hero-art" role="img" aria-label="Illustration of three colleagues at a desk with a laptop, celebrating beneath a large thumbs-up and a check mark"></div>

<div class="abs logo">Velasto</div>
<nav class="abs nav"><span>ABOUT</span><span>FEATURES</span><span>INSIGHTS</span><span>CONTACT</span></nav>
<div class="abs login">
  <svg width="11" height="11" viewBox="0 0 12 12" fill="none" stroke="#111" stroke-width="1.3"><circle cx="6" cy="4" r="2.5"/><path d="M1.5 11.5c0-2.5 2-4 4.5-4s4.5 1.5 4.5 4"/></svg>LOGIN
</div>
<div class="btn demo-top">Request a demo</div>

<h1 class="abs hero-title">Improve <span class="outline">Your</span><br>Employee <span class="outline">Morale</span></h1>
<p class="abs hero-sub">We are here to help you boost your employees on a consistent basis</p>
<div class="btn get-started">Get started
  <svg class="arrow" viewBox="0 0 12 10" fill="none" stroke="#fff" stroke-width="1.6"><path d="M0 5h10M6 1l4 4-4 4"/></svg>
</div>
<div class="abs explainer">WATCH EXPLAINER
  <span class="play"><svg width="8" height="9" viewBox="0 0 8 9"><path d="M1 0.5l6 4-6 4z" fill="#fff"/></svg></span>
</div>
<div class="abs trusted">
  <span>Trusted By:</span>
  <span class="brand"><i class="sq"></i>Northwind</span>
  <span class="brand">Parcelo</span>
  <span class="brand">Searchly</span>
  <span class="brand">Shopwell</span>
</div>

<p class="abs eyebrow" style="top:762px">Our <span>Features</span></p>
<h2 class="abs section-title" style="top:782px">Velasto is Here To Help<br>Businesses Like Yours</h2>

<svg class="abs connector" viewBox="0 930 1200 1100" fill="none">
  <g stroke="#d8d2c8" stroke-width="1.5">
    <path d="M600 960 V1040 Q600 1060 580 1060 H350 Q330 1060 330 1080 V1400"/>
    <path d="M330 1420 V1450 Q330 1470 350 1470 H825 Q845 1470 845 1490"/>
    <path d="M886 1840 V1930 Q886 1950 866 1950 H358 Q338 1950 338 1970 V2000"/>
  </g>
  <path d="M585 950 L600 965 L615 950" stroke="#d8d2c8" stroke-width="1.5"/>
  <g fill="var(--orange)">
    <circle cx="600" cy="1060" r="4"/>
    <circle cx="330" cy="1422" r="4"/>
    <circle cx="845" cy="1466" r="4"/>
    <circle cx="886" cy="1910" r="4"/>
    <circle cx="386" cy="1950" r="4"/>
  </g>
</svg>

<div class="abs feature-art art1" role="img" aria-label="Illustration of a smiling man holding up an employee ID card"></div>
<div class="abs orange-dot" style="left:438px;top:1078px;width:48px;height:48px"></div>
<div class="abs" style="left:676px;top:1094px">
  <p class="f-label">It's important to</p>
  <h3 class="f-title" style="margin-top:6px">Increase Employee<br>Retention</h3>
  <p class="f-body" style="margin-top:18px">Lorem ipsum dolor sit amet, consectetuer adipiscing elit, sed diam nonummy nibh euismod tincidunt ut laoreet dolore magna aliquam erat volutpat.</p>
</div>
<div class="btn" style="left:676px;top:1312px">Request a demo</div>

<div class="abs feature-art art2" role="img" aria-label="Illustration of a man working on a laptop with floating calendar and message icons"></div>
<div class="abs art2-base"></div>
<div class="abs orange-dot" style="left:862px;top:1508px;width:48px;height:48px"></div>
<div class="abs" style="left:137px;top:1582px">
  <p class="f-label">Modern alternative</p>
  <h3 class="f-title" style="margin-top:6px">From Raffles To<br>Auctions</h3>
  <p class="f-body" style="margin-top:18px">Lorem ipsum dolor sit amet, consectetuer adipiscing elit, sed diam nonummy nibh euismod tincidunt ut laoreet dolore magna aliquam erat volutpat.</p>
</div>
<div class="btn" style="left:137px;top:1799px">Request a demo</div>

<div class="abs feature-art art3" role="img" aria-label="Illustration of two photos: a bored worker labelled from this, and happy colleagues labelled to this"></div>
<div class="abs orange-dot" style="left:302px;top:1996px;width:48px;height:48px"></div>
<div class="abs" style="left:676px;top:2068px">
  <p class="f-label">Boost employee morale</p>
  <h3 class="f-title" style="margin-top:6px">And Transform<br>Your Work Events</h3>
  <p class="f-body" style="margin-top:18px">Lorem ipsum dolor sit amet, consectetuer adipiscing elit, sed diam nonummy nibh euismod tincidunt ut laoreet dolore magna aliquam erat volutpat.</p>
</div>
<div class="btn" style="left:676px;top:2287px">Request a demo</div>

<div class="abs about-box"></div>
<p class="abs eyebrow" style="top:2570px">About <span>Us</span></p>
<h2 class="abs section-title about-title">Start Building Your Event<br>Today With Velasto!</h2>
<div class="btn" style="left:525px;top:2730px;height:40px">Get started
  <svg class="arrow" viewBox="0 0 12 10" fill="none" stroke="#fff" stroke-width="1.6"><path d="M0 5h10M6 1l4 4-4 4"/></svg>
</div>
<div class="abs planner-art" role="img" aria-label="Illustration of an event planner dashboard with contact list, messages, schedule, calendar, e-mail and task panels"></div>

<p class="abs eyebrow" style="top:3335px">Client <span>Reviews</span></p>
<h2 class="abs section-title" style="top:3356px">What People Love About Velasto</h2>

<article class="abs review" style="left:60px">
  <p class="stars">★★★★★</p>
  <h4 class="r-title">Awesome Results.</h4>
  <p class="r-body">Lorem ipsum dolor sit amet, consectetuer adipiscing elit, sed diam nonummy nibh euismod tincidunt ut laoreet dolore magna aliquam erat volutpat. Ut wisi enim ad minim veniam, quis nostrud exerci tation ullamcorper suscipit lobortis nisl ut aliquip ex ea commodo consequat.</p>
  <p class="r-name">Nora Hale</p>
  <p class="r-role">Company Name, CEO</p>
  <span class="quote">”</span>
</article>
<article class="abs review" style="left:428px">
  <p class="stars">★★★★★</p>
  <h4 class="r-title">Awesome Results.</h4>
  <p class="r-body">Lorem ipsum dolor sit amet, consectetuer adipiscing elit, sed diam nonummy nibh euismod tincidunt ut laoreet dolore magna aliquam erat volutpat. Ut wisi enim ad minim veniam, quis nostrud exerci tation ullamcorper suscipit lobortis nisl ut aliquip ex ea commodo consequat.</p>
  <p class="r-name">Nora Hale</p>
  <p class="r-role">Company Name, CEO</p>
  <span class="quote">”</span>
</article>
<article class="abs review" style="left:795px">
  <p class="stars">★★★★★</p>
  <h4 class="r-title">Awesome Results.</h4>
  <p class="r-body">Lorem ipsum dolor sit amet, consectetuer adipiscing elit, sed diam nonummy nibh euismod tincidunt ut laoreet dolore magna aliquam erat volutpat. Ut wisi enim ad minim veniam, quis nostrud exerci tation ullamcorper suscipit lobortis nisl ut aliquip ex ea commodo consequat.</p>
  <p class="r-name">Nora Hale</p>
  <p class="r-role">Company Name, CEO</p>
  <span class="quote">”</span>
</article>

<svg class="abs news-band" viewBox="0 0 1200 420" preserveAspectRatio="none">
  <path d="M0 250 Q600 -60 1200 250 V420 H0z" fill="#efeae3"/>
  <path d="M0 270 Q600 -30 1200 270 V420 H0z" fill="#ffffff"/>
</svg>
<h2 class="abs section-title news-title">Get Weekly Updates About Us</h2>
<div class="abs subscribe">Your Email Address
  <div class="btn">Subscribe</div>
</div>

<nav class="abs footer-nav"><span>ABOUT</span><span>FEATURES</span><span>INSIGHTS</span><span>CONTACT</span></nav>
<div class="abs socials"><span></span><span></span><span></span></div>
<p class="abs copy">© Velasto - 2022. All Rights Reserved.</p>

</body>
</html>
```